Pine Ridge Dwellings Stationary and Simplified Embroidery Contest
Business Card, Letterhead, Envelope, Note Pad, Sticker, Embroidery
Pine Ridge Dwellings Stationary and Simplified Embroidery Contest -
Creative Brief
Professional
Wendell Marsh
Construction Manager
4812 Galloway Street Edmonton AB T5K 3R8
wendell@pineridgedwellings.example
www.pineridgedwellings.example
Please include some with light backgrounds as well as dark options... we want to be able to print a few cards so that not every card we hand out is the same! I would like to have 4-6 business card designs. The embroidery part would just be a simplified logo.
Comments/Blank space for notes to written on the business card. We have looked at a few designs for business cards and like the Logo and Name on the front with all the details on the back, but do be creative with this is by no means a rule!

```html
<!DOCTYPE html>
<html lang="en">
<head>
<meta charset="utf-8">
<title>Pine Ridge Dwellings Stationery</title>
<link rel="stylesheet" href="https://fonts.googleapis.com/css2?family=Cinzel:wght@600&family=Open+Sans:wght@400;600&display=swap">
<style>
  :root{
    --backdrop:#e9dcc6;
    --backdrop-edge:#dccaa9;
    --paper:#ffffff;
    --orange:#e0911c;
    --orange-deep:#b8690c;
    --green:#4c5a3e;
    --green-deep:#38432d;
    --ink:#3d3a35;
    --label:#8a7458;
    --faint:#f3e3c6;
  }
  *{margin:0;padding:0;box-sizing:border-box}
  html,body{width:1200px;height:446px;overflow:hidden}
  body{
    position:relative;
    background:radial-gradient(ellipse at 50% 40%, var(--backdrop) 55%, var(--backdrop-edge) 100%);
    font-family:"Open Sans",Arial,sans-serif;
    color:var(--ink);
  }
  .piece{position:absolute;box-shadow:0 2px 5px rgba(0,0,0,.25);background:var(--paper)}
  .piece svg{display:block;width:100%;height:100%}
  .label{
    position:absolute;font-size:7px;letter-spacing:.8px;text-transform:uppercase;
    color:var(--label);white-space:nowrap
  }
  .brand{font-family:"Cinzel",Georgia,serif;font-weight:600;fill:var(--ink)}
  .detail{font-family:"Open Sans",Arial,sans-serif;fill:var(--ink)}
  .card-front{left:12px;top:166px;width:100px;height:60px}
  .card-back{left:12px;top:257px;width:100px;height:60px}
  .letterhead-one{left:139px;top:14px;width:317px;height:413px}
  .letterhead-two{left:475px;top:14px;width:317px;height:413px}
  .envelope-back-orange{left:809px;top:17px;width:386px;height:88px}
  .envelope-back-green{left:809px;top:108px;width:386px;height:86px}
  .envelope-back-white{left:809px;top:197px;width:386px;height:84px}
  .envelope-front{left:797px;top:290px;width:398px;height:130px}
</style>
</head>
<body>

<span class="label" style="left:6px;top:130px">Business Cards</span>

<div class="piece card-front">
  <svg viewBox="0 0 100 60">
    <rect width="100" height="60" fill="var(--faint)"/>
    <circle cx="50" cy="30" r="26" fill="none" stroke="var(--orange)" stroke-width="1.2" opacity=".7"/>
    <circle cx="50" cy="24" r="5" fill="var(--green)"/>
    <text class="brand" x="50" y="38" font-size="5.2" text-anchor="middle">Pine Ridge Dwellings</text>
  </svg>
</div>
<span class="label" style="left:12px;top:238px">Business Card Front</span>

<div class="piece card-back">
  <svg viewBox="0 0 100 60">
    <rect width="100" height="60" fill="#fdf6e8"/>
    <rect x="4" y="4" width="92" height="52" fill="none" stroke="var(--orange)" stroke-width=".8"/>
    <g stroke="var(--orange)" stroke-width=".4" opacity=".7">
      <line x1="10" y1="18" x2="90" y2="18"/>
      <line x1="10" y1="26" x2="90" y2="26"/>
      <line x1="10" y1="34" x2="90" y2="34"/>
      <line x1="10" y1="42" x2="90" y2="42"/>
      <line x1="10" y1="50" x2="90" y2="50"/>
    </g>
  </svg>
</div>
<span class="label" style="left:12px;top:329px">Business Card Back</span>

<!-- Letterhead option 1 -->
<div class="piece letterhead-one">
  <svg viewBox="0 0 317 413">
    <path d="M0 0H317V8C230 6 120 18 0 42Z" fill="var(--orange)"/>
    <path d="M0 42C120 18 230 6 317 8V12C230 11 120 22 0 47Z" fill="var(--green)"/>
    <circle cx="36" cy="28" r="5" fill="var(--green)"/>
    <text class="brand" x="44" y="30" font-size="6">Pine Ridge Dwellings</text>
    <g class="detail" font-size="3.6">
      <text x="230" y="30">4812 Galloway Street</text>
      <text x="230" y="36">Edmonton AB T5K 3R8</text>
      <text x="230" y="42">wendell@pineridgedwellings.example</text>
      <text x="230" y="48">www.pineridgedwellings.example</text>
    </g>
    <circle cx="158" cy="170" r="60" fill="var(--faint)" opacity=".6" role="img" aria-label="Faint brand emblem watermark"/>
    <path d="M0 360C90 380 200 400 317 340V413H0Z" fill="var(--green)"/>
    <path d="M0 372C100 392 210 410 317 352V413H0Z" fill="var(--orange)"/>
  </svg>
</div>
<span class="label" style="left:268px;top:432px">Letter Head Option 1</span>

<!-- Letterhead option 2 -->
<div class="piece letterhead-two">
  <svg viewBox="0 0 317 413">
    <path d="M0 0H317V6C220 8 110 14 0 30Z" fill="var(--orange)"/>
    <path d="M0 30C110 14 220 8 317 6V9C220 12 110 18 0 34Z" fill="var(--green)"/>
    <circle cx="36" cy="26" r="5" fill="var(--green)"/>
    <text class="brand" x="44" y="28" font-size="6">Pine Ridge Dwellings</text>
    <circle cx="158" cy="170" r="60" fill="var(--faint)" opacity=".6" role="img" aria-label="Faint brand emblem watermark"/>
    <path d="M0 350C110 395 220 390 317 330V413H0Z" fill="var(--green)"/>
    <path d="M0 362C110 405 225 402 317 344V413H0Z" fill="var(--orange)"/>
  </svg>
</div>
<span class="label" style="left:604px;top:432px">Letter Head Option 2</span>

<!-- Envelopes -->
<div class="piece envelope-back-orange">
  <svg viewBox="0 0 386 88">
    <rect width="386" height="88" fill="#fbfbf9"/>
    <path d="M0 0H386V22L193 60L0 22Z" fill="var(--orange)"/>
    <circle cx="193" cy="36" r="7" fill="var(--green)"/>
  </svg>
</div>
<div class="piece envelope-back-green">
  <svg viewBox="0 0 386 86">
    <rect width="386" height="86" fill="#fbfbf9"/>
    <path d="M0 0H386V24L193 62L0 24Z" fill="var(--green)"/>
    <circle cx="193" cy="36" r="7" fill="var(--orange)"/>
  </svg>
</div>
<div class="piece envelope-back-white">
  <svg viewBox="0 0 386 84">
    <rect width="386" height="84" fill="#fbfbf9"/>
    <path d="M0 0H386V14L193 34L0 14Z" fill="#f1f1ee" stroke="#ddd" stroke-width=".6"/>
    <circle cx="193" cy="24" r="6" fill="var(--green)"/>
  </svg>
</div>
<div class="piece envelope-front">
  <svg viewBox="0 0 398 130">
    <rect width="398" height="130" fill="var(--paper)"/>
    <path d="M0 0H140C90 6 40 10 0 22Z" fill="var(--orange)"/>
    <circle cx="22" cy="32" r="5" fill="var(--green)"/>
    <text class="brand" x="30" y="34" font-size="6">Pine Ridge Dwellings</text>
    <text class="detail" x="30" y="41" font-size="3.6">4812 Galloway Street Edmonton AB T5K 3R8</text>
    <path d="M398 70C300 110 150 122 0 118V130H398Z" fill="var(--green)"/>
    <path d="M398 82C300 118 150 128 0 126V130H398Z" fill="var(--orange)"/>
  </svg>
</div>
<span class="label" style="left:1090px;top:432px">Envelope Design</span>

</body>
</html>
```